Virtual Restaurant Menu Design

I need a menu displayed on monitors of my casual restaurant. I currently have 3 monitors, I could potentially add 2 more. My menu is quite large but I need the monitors to each display part of the menu in a manner that is visually appealing but still easy to read. That means there needs to be 3 separate files where one file will be displayed on one monitor and the other two files on the the other monitors. Looking for a classic and clean look. I have attached menu for reference. Including some professional pictures incase you can incorporate them into the design for that section. Catering and beverage section of menu need not be displayed. I would like an editable version of this incase my prices change in the future.Good performance on this will very likely lead to future work as I have specials that I like to change and display on a monthly basis.
Italian Restaurant

```html
<!DOCTYPE html>
<html lang="en">
<head>
<meta charset="utf-8">
<title>Chicken &amp; Veal Menu Board</title>
<link rel="stylesheet" href="https://fonts.googleapis.com/css2?family=Sorts+Mill+Goudy&family=Varela+Round&display=swap">
<style>
  :root {
    --header-red: #9a3a2c;
    --header-red-dark: #6e2c1c;
    --header-red-bright: #b8321f;
    --band-green: #3f6b2a;
    --band-green-dark: #2d5a1c;
    --parchment: #e2e0ac;
    --parchment-light: #eae8bf;
    --gold: #d9c98e;
    --ink: #1c1c14;
    --dish-red: #a3161a;
    --white: #ffffff;
    --ornament: #b8493a;
    --photo-dark: #2b2824;
    --photo-brown: #5e4030;
    --photo-warm: #b87a3e;
  }
  * { margin: 0; padding: 0; box-sizing: border-box; }
  html, body { width: 1200px; height: 900px; overflow: hidden; }
  body { font-family: "Varela Round", "Verdana", sans-serif; color: var(--ink); }

  .menu-board {
    position: relative;
    width: 1200px;
    height: 900px;
    overflow: hidden;
    background:
      linear-gradient(90deg, rgba(79,138,46,0.8) 0%, rgba(79,138,46,0.25) 16%, rgba(0,0,0,0) 36%, rgba(0,0,0,0) 64%, rgba(194,74,42,0.25) 84%, rgba(194,74,42,0.75) 100%),
      radial-gradient(ellipse at 50% 40%, var(--parchment-light) 0%, var(--parchment) 70%);
  }

  .board-header {
    position: absolute; left: 0; top: 0;
    width: 1200px; height: 170px;
    background: linear-gradient(90deg, var(--header-red-dark) 0%, var(--header-red) 40%, var(--header-red) 70%, var(--header-red-bright) 100%);
    font-family: "Sorts Mill Goudy", "Georgia", serif;
    color: var(--gold);
  }
  .board-title {
    position: absolute; left: 0; top: 22px;
    width: 1164px;
    text-align: center;
    font-size: 85px; font-weight: 400; line-height: 1;
    letter-spacing: 1px;
  }
  .board-subtitle {
    position: absolute; left: 0; top: 98px;
    width: 1164px;
    text-align: center;
    font-size: 45px; line-height: 1;
  }

  .price-band {
    position: absolute; left: 0; top: 170px;
    width: 1200px; height: 46px;
    background: linear-gradient(90deg, var(--band-green-dark) 0%, var(--band-green) 50%, #5a6a2e 100%);
    display: flex; justify-content: center; align-items: center; gap: 70px;
    font-size: 26.5px; letter-spacing: 0.5px;
    padding-right: 28px;
  }
  .price-band .price { color: var(--white); }

  .dish-list {
    position: absolute; left: 76px; top: 321px;
    list-style: none;
    font-size: 24px; line-height: 27px; letter-spacing: 0.3px;
  }
  .dish { margin-bottom: 28px; }
  .dish-name { color: var(--dish-red); font-weight: 700; }

  .feature-photo {
    position: absolute; left: 599px; top: 314px;
    width: 601px; height: 408px;
    background: linear-gradient(170deg, var(--photo-dark) 0%, var(--photo-brown) 45%, var(--photo-warm) 100%);
  }
  .feature-caption {
    position: absolute; left: 700px; top: 738px;
    width: 376px; text-align: center;
    font-size: 26px; letter-spacing: 0.5px;
  }

  .ornament {
    position: absolute; left: 364px; top: 764px;
    width: 420px; height: 96px;
  }
</style>
</head>
<body>
  <main class="menu-board">
    <header class="board-header">
      <h1 class="board-title">CHICKEN &amp; VEAL</h1>
      <p class="board-subtitle">Includes a side salad &amp; garlic bread</p>
    </header>

    <div class="price-band">
      <span>CHICKEN ENTREES <span class="price">17.50</span></span>
      <span>VEAL ENTREES <span class="price">19.95</span></span>
    </div>

    <ul class="dish-list">
      <li class="dish"><span class="dish-name">Piccata</span> With capers sauteed<br>in a white garlic lemon sauce</li>
      <li class="dish"><span class="dish-name">Marsala</span> With mushrooms<br>in Marsala wine sauce</li>
      <li class="dish"><span class="dish-name">Parmigiana</span> Topped with<br>mozzarella &amp; tomato sauce</li>
      <li class="dish"><span class="dish-name">Al Pesto</span> Sauteed with mushrooms<br>in creamy pesto sauce, served over penne</li>
      <li class="dish"><span class="dish-name">Brunello</span> Mushrooms &amp; Sun-dried<br>tomatoes in creamy pink sauce</li>
    </ul>

    <div class="feature-photo" role="img" aria-label="Photo of chicken brunello: penne with chicken, mushrooms and sun-dried tomatoes in a pink sauce"></div>
    <p class="feature-caption">CHICKEN BRUNELLO</p>

    <svg class="ornament" viewBox="0 0 420 96" role="img" aria-label="Decorative scroll flourish">
      <rect x="0" y="30" width="420" height="56" rx="28" fill="var(--ornament)" opacity="0.3"/>
    </svg>
  </main>
</body>
</html>
```